We need a DL size flyer, double sided, for our lawn mowing and gardening business, Kestrel Greens.

We want to run on the front side, the following promotion:
50% off lawn mowing, applies to first lawn mowed on any regular service,
applies to first 100 callers only, so call now!
Professional lawn mowing at an affordable price.

Logo at the bottom left, with Lawn and Garden Maintenance written just below logo.

On bottom Right contact details;
Tom and Gareth
Ph: 0487650912
Email: kestrelgreens@mailbox-example.com
www.kestrelgreens-example.com.au

Front side positioned horizontally, with a bright and colour full design in the background, with the offer of 50% Off lawn mowing in large letters along the top.

On the rear side, also positioned horizontally, a list of our services, stating;

At Kestrel Greens we specialise in the following services;
Lawn mowing
Edging
Blowing
Hedging
Pruning
Tree Loping
Weeding
Poisoning
Mulching
Fertilising
Rubbish removal
Planting
Lawn care and advice
Turf
And any other garden maintenance job,
No job too big or too small.
(No particular order, whatever fits best)
Also include our contact details,
Kestrel Greens
Ph 0487650912
www.kestrelgreens-example.com.au

Target Market(s)

Home owners, aged between 30-50 years old, moderate socio ecenomic status to more afluent areas.

Industry/Entity Type

Business

Requirements
Must have
• DL size, front and back, full colour.
Nice to have
• The writting stating "Kestrel Greens" in our logo is quite bland, if that could also be amended to make it more appealing, but change the writting design only not the actual logo.

```html
<!DOCTYPE html>
<html lang="en">
<head>
<meta charset="utf-8">
<title>Kestrel Greens – Services Flyer (Rear)</title>
<link rel="stylesheet" href="https://fonts.googleapis.com/css2?family=Oswald:wght@500;600&family=Noto+Sans:wght@700&display=swap">
<style>
  :root {
    --stage: #2e2e2e;
    --brand-green: #16953b;
    --ink: #1c1c1c;
    --sky: #b9d7e6;
    --mist: #eef2ea;
    --meadow: #d9d7b4;
    --earth: #b9b587;
    --strip: #ffffff;
  }
  * { margin: 0; padding: 0; box-sizing: border-box; }
  html, body {
    width: 1200px;
    height: 900px;
    overflow: hidden;
    background: var(--stage);
  }
  .flyer {
    position: absolute;
    left: 40px;
    top: 170px;
    width: 1120px;
    height: 560px;
    background: var(--strip);
    overflow: hidden;
  }
  .flyer__panel {
    position: absolute;
    left: 0; top: 0;
    width: 100%;
    height: 483px;
    background:
      radial-gradient(ellipse 60% 55% at 12% 5%, var(--sky) 0%, transparent 70%),
      radial-gradient(ellipse 50% 60% at 95% 55%, #c9cfd9 0%, transparent 70%),
      linear-gradient(180deg, #dfe9ec 0%, var(--mist) 30%, #e8e9d6 58%, var(--meadow) 80%, var(--earth) 100%);
  }
  .flyer__heading {
    position: absolute;
    left: 0; right: 0;
    top: 48px;
    text-align: center;
    font-family: "Oswald", sans-serif;
    font-weight: 600;
    font-size: 40px;
    letter-spacing: -0.2px;
    color: var(--brand-green);
    white-space: nowrap;
  }
  .service-list {
    position: absolute;
    top: 120px;
    list-style: none;
    font-family: "Noto Sans", sans-serif;
    font-weight: 700;
    font-size: 29px;
    line-height: 47.5px;
    color: var(--ink);
    white-space: nowrap;
  }
  .service-list--a { left: 73px; }
  .service-list--b { left: 386px; }
  .service-list--c { left: 667px; }
  .service-list li { display: flex; align-items: center; }
  .service-list li::before {
    content: "";
    width: 11px; height: 11px;
    margin: 0 11px 0 4px;
    background: var(--brand-green);
    transform: rotate(45deg);
    flex: none;
  }
  .flyer__closing {
    position: absolute;
    left: 0; right: 0;
    top: 378px;
    text-align: center;
    font-family: "Noto Sans", sans-serif;
    font-weight: 700;
    font-size: 21px;
    line-height: 31px;
    color: var(--brand-green);
    text-transform: uppercase;
  }
  .flyer__contact {
    position: absolute;
    left: 0; right: 0;
    bottom: 0;
    height: 77px;
    display: flex;
    align-items: center;
    justify-content: center;
    gap: 18px;
    font-family: "Oswald", sans-serif;
    font-weight: 500;
    font-size: 25px;
    color: var(--brand-green);
  }
  .flyer__contact .divider { font-weight: 500; }
</style>
</head>
<body>
  <main class="flyer">
    <section class="flyer__panel">
      <h1 class="flyer__heading">At Kestrel Greens we specialise in the following services:</h1>

      <ul class="service-list service-list--a">
        <li>Lawn mowing</li>
        <li>Edging</li>
        <li>Blowing</li>
        <li>Hedging</li>
        <li>Pruning</li>
      </ul>
      <ul class="service-list service-list--b">
        <li>Tree Loping</li>
        <li>Weeding</li>
        <li>Poisoning</li>
        <li>Mulching</li>
        <li>Fertilising</li>
      </ul>
      <ul class="service-list service-list--c">
        <li>Rubbish removal</li>
        <li>Planting</li>
        <li>Lawn care and advice</li>
        <li>Turf</li>
      </ul>

      <p class="flyer__closing">
        And any other garden maintenance job,<br>
        No job too big or too small.<br>
        (No particular order, whatever fits best)
      </p>
    </section>

    <footer class="flyer__contact">
      <span>Kestrel Greens</span>
      <span class="divider">|</span>
      <span>Ph 048.765.0912</span>
      <span class="divider">|</span>
      <span>www.kestrelgreens-example.com.au</span>
    </footer>
  </main>
</body>
</html>
```